CD Cover Art!

I am releasing an EP (3 song CD) and a full length CD (9 songs) and would like to have 2 distinct yet somehow tied together CD covers... they could be tied together through a simple color scheme or via tricky titles or through a shared logo designed around my name (Dane Harlow) or some other method of your imagination. I am not expecting two distinctly different covers, please design one and borrow from it to design the other which should simply the design greatly and insure I have no problem branding myself.

I will have some photos you can use soon or look at www.ravenbarker.example for some ideas although please be aware these CD's are not for Dane Harlow and The Drifters... this is design is for just "Dane Harlow"

My new Website should be up soon, please check it for design references www.DaneHarlow.example

Reason: Due to lack of designs submissions I've increased the budget and am guaranteeing payment, this is my first time using a service like this so I'm just learning the ropes!

Target Market(s)

Rock and Blues music lovers.

Font styles to use
Other font styles liked:
• Earth Kid

Requirements
Must have
• Title and or logo on both CD's

Name of the EP CD will be "Velvet Horizon" and the full length CD will be called "Dane Harlow Collection"
"Earth Kid" is the name of the font used on my website, I'd like to use it for consistency on both CD Covers.
Nice to have
• I love crosses and birds of prey, motorcycles and I really like Morrow's album art although I am not latino and wouldn't want a latino-style. I just love the colors and art-work. My design does not have to have any one or all of these items but I like them!

If desired I can provide a picture of my motorcycle if you are going to include one in the design it might as well be mine.

```html
<!DOCTYPE html>
<html lang="en">
<head>
<meta charset="utf-8">
<title>Dane Harlow – CD Covers</title>
<link href="https://fonts.googleapis.com/css2?family=Italianno&family=Stardos+Stencil:wght@700&display=swap" rel="stylesheet">
<style>
  :root {
    --paper: #ffffff;
    --band: #858789;
    --title-orange: #e8741c;
    --title-glow: rgba(255, 210, 140, 0.55);
    --stencil-white: #fdf6ea;
    --stencil-orange: #f08a1e;
    --photo-deep: #3a1e0e;
    --photo-mid: #9a4a18;
    --photo-warm: #e79a3c;
    --photo-light: #f7e2bc;
  }
  * { margin: 0; padding: 0; box-sizing: border-box; }
  html, body {
    width: 1200px;
    height: 848px;
    overflow: hidden;
    background: var(--paper);
  }
  .sheet {
    position: relative;
    width: 1200px;
    height: 848px;
  }
  .cover {
    position: absolute;
    top: 103px;
    height: 515px;
    overflow: hidden;
  }
  .cover--ep { left: 71px; width: 515px; }
  .cover--album { left: 650px; width: 480px; }

  .cover__photo {
    position: absolute;
    inset: 0;
  }
  .cover--ep .cover__photo {
    background:
      radial-gradient(ellipse 55% 45% at 62% 40%, var(--photo-light) 0%, rgba(247,226,188,0) 70%),
      radial-gradient(ellipse 70% 60% at 40% 65%, var(--photo-warm) 0%, rgba(231,154,60,0) 75%),
      linear-gradient(160deg, var(--photo-mid) 0%, var(--photo-deep) 55%, var(--photo-mid) 100%);
  }
  .cover--album .cover__photo {
    background:
      radial-gradient(ellipse 40% 35% at 45% 30%, #fff7ea 0%, rgba(255,247,234,0) 75%),
      radial-gradient(ellipse 60% 40% at 55% 75%, var(--photo-deep) 0%, rgba(58,30,14,0) 80%),
      linear-gradient(120deg, var(--photo-warm) 0%, var(--photo-light) 35%, var(--photo-mid) 70%, var(--photo-warm) 100%);
  }

  .cover__title {
    position: absolute;
    left: 0;
    right: 0;
    top: 228px;
    text-align: center;
    font-family: "Italianno", cursive;
    font-size: 104px;
    line-height: 1;
    color: var(--title-orange);
    text-shadow: 0 0 6px var(--title-glow);
  }
  .cover--album .cover__title { left: 10px; right: auto; width: 420px; }

  .cover__edition {
    position: absolute;
    left: 0;
    right: 0;
    bottom: 22px;
    text-align: center;
    font-family: "Stardos Stencil", sans-serif;
    font-weight: 700;
    font-size: 34px;
    letter-spacing: 9px;
    color: var(--stencil-white);
    text-transform: uppercase;
  }
  .cover__series {
    position: absolute;
    top: 0;
    right: 4px;
    height: 515px;
    width: 56px;
    writing-mode: vertical-rl;
    transform: rotate(180deg);
    text-align: center;
    font-family: "Stardos Stencil", sans-serif;
    font-weight: 700;
    font-size: 44px;
    letter-spacing: 7px;
    line-height: 56px;
    color: var(--stencil-orange);
    text-transform: uppercase;
  }

  .footer-band {
    position: absolute;
    left: 71px;
    top: 695px;
    width: 1059px;
    height: 103px;
    background: var(--band);
  }
</style>
</head>
<body>
  <main class="sheet">
    <section class="cover cover--ep" aria-label="EP cover: Velvet Horizon">
      <div class="cover__photo" role="img" aria-label="Warm amber-toned close-up photo of hands playing an electric guitar"></div>
      <h1 class="cover__title">Dane Harlow</h1>
      <p class="cover__edition">Velvet Horizon</p>
    </section>

    <section class="cover cover--album" aria-label="Album cover: Dane Harlow Collection">
      <div class="cover__photo" role="img" aria-label="Warm amber-toned photo of a musician in a white shirt playing an electric guitar"></div>
      <h2 class="cover__title">Dane Harlow</h2>
      <p class="cover__series">Collection</p>
    </section>

    <div class="footer-band" aria-hidden="true"></div>
  </main>
</body>
</html>
```